Liam Kovac Fitness Business Card

I Need a really cool and creative yet modern and cutting edge. I run a personal training company, I have a logo already which ill submit images of. Id like the base colors to be black and white with a little red as a highlight color. Charcoal grey is fine also. My clientele is mostly comprised of young professionals who are in touch with modern culture art and are interested in "cool" so if there was one thing i want this business card to be it sexy and cool.

Target Market(s)

young professionals who are image conscious, care about their health, looking and feeling good. They know what is cool and expect the best.

Industry/Entity Type

Training

Requirements
Must have
• - must be a 2 sided card
- must include the following:

Liam Kovac CPT
646 392 7105
Liam@LiamKovacFitness.example
www.LiamKovacFitness.example
Nice to have
• id like to see some unconventional shape ideas as well as conventional ones

```html
<!DOCTYPE html>
<html lang="en">
<head>
<meta charset="utf-8">
<title>Liam Kovac Fitness – Business Card</title>
<link rel="stylesheet" href="https://fonts.googleapis.com/css2?family=Didact+Gothic&display=swap">
<style>
  :root {
    --ink: #0b0b0b;
    --paper: #ffffff;
    --signal-red: #e10613;
    --fold-light: #f4f4f4;
    --fold-mid: #c9c9c9;
    --fold-dark: #8f8f8f;
    --type: "Didact Gothic", sans-serif;
  }
  * { margin: 0; padding: 0; box-sizing: border-box; }
  html, body { width: 1200px; height: 800px; overflow: hidden; background: var(--paper); }
  .canvas { position: relative; width: 1200px; height: 800px; font-family: var(--type); }

  .card {
    position: absolute;
    width: 520px;
    height: 300px;
    overflow: hidden;
    box-shadow: 0 6px 18px rgba(0,0,0,0.18);
  }
  .card--front { left: 70px; top: 130px; background: var(--ink); }
  .card--back  { left: 610px; top: 370px; background: var(--signal-red); }

  .card__fold { position: absolute; inset: 0; width: 520px; height: 300px; }

  .wordmark {
    position: absolute;
    display: flex;
    align-items: center;
    gap: 8px;
    color: var(--ink);
    font-size: 21px;
    letter-spacing: 0.2px;
    white-space: nowrap;
  }
  .wordmark__dot { width: 12px; height: 12px; border-radius: 50%; background: var(--signal-red); }
  .card--front .wordmark { left: 318px; top: 176px; }
  .card--back .wordmark { left: 292px; top: 96px; }
  .card--back .wordmark__dot { background: var(--ink); }

  .front-details { position: absolute; left: 44px; top: 92px; color: var(--paper); }
  .front-details__name { font-size: 24px; margin-bottom: 26px; }
  .front-details__line { font-size: 17px; line-height: 21px; }

  .back-name { position: absolute; left: 34px; top: 118px; color: var(--ink); font-size: 22px; line-height: 27px; }

  .back-contact {
    position: absolute; right: 34px; bottom: 34px;
    color: var(--ink); font-size: 16px; line-height: 20px; text-align: right;
  }
</style>
</head>
<body>
<main class="canvas">

  <section class="card card--front" aria-label="Front of card">
    <svg class="card__fold" viewBox="0 0 520 300" aria-hidden="true">
      <defs>
        <linearGradient id="fold-front" x1="0" y1="0" x2="1" y2="0.4">
          <stop offset="0" stop-color="var(--fold-dark)"/>
          <stop offset="0.35" stop-color="var(--fold-mid)"/>
          <stop offset="0.7" stop-color="var(--fold-light)"/>
          <stop offset="1" stop-color="#ffffff"/>
        </linearGradient>
      </defs>
      <path d="M300,0 L520,0 L520,300 L262,300 C325,235 352,120 300,0 Z" fill="url(#fold-front)"/>
      <path d="M300,0 C352,120 325,235 262,300" fill="none" stroke="#ffffff" stroke-width="3"/>
    </svg>
    <div class="front-details">
      <p class="front-details__name">Liam Kovac CPT</p>
      <p class="front-details__line">646 392 7105</p>
      <p class="front-details__line">Liam@LiamKovacFitness.example</p>
      <p class="front-details__line">www.LiamKovacFitness.example</p>
    </div>
    <div class="wordmark"><span class="wordmark__dot"></span>Liam Kovac Fitness</div>
  </section>

  <section class="card card--back" aria-label="Back of card">
    <svg class="card__fold" viewBox="0 0 520 300" aria-hidden="true">
      <defs>
        <linearGradient id="fold-back" x1="1" y1="0" x2="0" y2="0.6">
          <stop offset="0" stop-color="var(--fold-dark)"/>
          <stop offset="0.4" stop-color="var(--fold-mid)"/>
          <stop offset="0.75" stop-color="var(--fold-light)"/>
          <stop offset="1" stop-color="#ffffff"/>
        </linearGradient>
      </defs>
      <path d="M0,0 L236,0 C182,70 170,200 238,300 L0,300 Z" fill="url(#fold-back)"/>
      <path d="M236,0 C182,70 170,200 238,300" fill="none" stroke="#ffffff" stroke-width="3"/>
    </svg>
    <p class="back-name">Liam Kovac<br>CPT</p>
    <div class="wordmark"><span class="wordmark__dot"></span>Liam Kovac Fitness</div>
    <div class="back-contact">
      <p>646 392 7105</p>
      <p>Liam@LiamKovacFitness.example</p>
      <p>www.LiamKovacFitness.example</p>
    </div>
  </section>

</main>
</body>
</html>
```